One page responsive Wordpress Website

I am looking to design and code for 1-page Wordpress responsive website (desktop/mobile/tablet). Pls see attached file. Job scope includes Wordpress design and coding of the actual Live website
Target Market(s)
Small medium business
Industry/Entity Type
Telecommunications
Font styles to use
Sans Serif
Colors
ffffff
85cae6
63bae0
33a6d7
cedeed
3277b5
Requirements
Must have
- One page only, Wordpress, Responsive layout in desktop, mobile, tablet

```html
<!DOCTYPE html>
<html lang="en">
<head>
<meta charset="utf-8">
<title>Calvera IP Phone</title>
<link href="https://fonts.googleapis.com/css2?family=Roboto:wght@400;500;700&display=swap" rel="stylesheet">
<style>
:root{
  --blue-deep:#1479dc;
  --blue:#1a8de6;
  --blue-bright:#33a6d7;
  --blue-sky:#63bae0;
  --blue-pale:#85cae6;
  --mist:#cedeed;
  --white:#ffffff;
  --ink:#111111;
  --text:#222222;
  --muted:#8a8f96;
  --rule:#d8dbe0;
  --device:#2b323d;
}
*{margin:0;padding:0;box-sizing:border-box}
html,body{width:721px;height:1200px;overflow:hidden;background:var(--white)}
body{position:relative;font-family:'Roboto',sans-serif;color:var(--text)}
.abs{position:absolute}

/* about photo + hero curve */
.about-photo{left:0;top:400px;width:721px;height:380px;
  background:linear-gradient(100deg,#eef1f4 0%,#e3e7eb 45%,#9aa3ad 70%,#3a4250 85%,#2a303a 100%)}
.hero{left:0;top:0;width:721px;height:500px}

.brand{left:67px;top:8px;font-size:21px;font-weight:700;color:var(--white)}
.nav{right:67px;top:14px;font-size:10px;font-weight:500;color:var(--white);display:flex;gap:16px}
.hero-kicker{left:0;width:721px;top:75px;text-align:center;color:var(--white);font-size:11.5px}
.hero-title{left:0;width:721px;top:96px;text-align:center;color:var(--white);font-size:29px;font-weight:700;letter-spacing:.3px}
.hero-lead{left:0;width:721px;top:136px;text-align:center;color:var(--white);font-size:9.6px;line-height:17.5px}

.product{width:200px;text-align:center}
.product h3{font-size:13.5px;font-weight:700;color:var(--white);margin-top:189px}
.product-image{width:110px;height:162px;margin:10px auto 0;border-radius:6px;
  background:linear-gradient(160deg,#3a4350,var(--device) 60%,#1c222b)}
.btn-sheet{display:block;width:158px;height:30px;margin:12px auto 0;border:1px solid var(--white);
  color:var(--white);font-size:9.5px;font-weight:700;line-height:28px}

.about{left:66px;top:530px;width:310px}
.about h2{font-size:21px;font-weight:700;color:var(--ink);margin-bottom:10px}
.about p{font-size:9.3px;line-height:17.5px;color:var(--text)}

/* contact */
.contact{left:0;top:780px;width:721px;height:252px;
  background:linear-gradient(120deg,#1f9be3 0%,#1a8fdc 50%,#1e9fe6 100%)}
.contact-copy{left:66px;top:838px;width:190px;color:var(--white)}
.contact-copy h2{font-size:19.5px;font-weight:700;line-height:24px}
.contact-copy h4{font-size:14px;font-weight:500;line-height:17.5px;margin-top:6px}
.contact-copy p{font-size:8.3px;line-height:13.4px;margin-top:9px}
.field{width:185px;height:30px;background:var(--white);border:1px solid var(--mist);
  font-size:8.5px;color:var(--muted);display:flex;align-items:center;gap:4px;padding-left:9px}
.field.message{width:184px;height:102px;align-items:flex-start;padding-top:10px}
.field svg{width:7px;height:7px;fill:#c5c9ce}
.submit{left:470px;top:944px;width:184px;height:30px;border:1.5px solid var(--white);color:var(--white);
  font-size:10px;font-weight:500;display:flex;align-items:center;justify-content:center;gap:6px}

/* footer */
.footer-brand{left:67px;top:1066px;font-size:21px;font-weight:700;color:var(--blue)}
.foot-col h5{font-size:11px;font-weight:700;color:var(--ink);margin-bottom:6px}
.foot-col li{list-style:none;font-size:10px;line-height:17.5px;color:#333}
.support li{display:flex;gap:8px;align-items:flex-start;margin-bottom:2px}
.support svg{width:8px;height:8px;margin-top:5px;fill:#333;flex:none}
.more li{display:flex;align-items:center;gap:6px;font-size:8.5px;margin-bottom:4px}
.more .dot{width:13px;height:13px;border-radius:50%;background:#eef0f3}
.rule{left:67px;top:1170px;width:588px;height:1px;background:var(--rule)}
.copyright{left:0;width:721px;top:1178px;text-align:center;font-size:9.5px;color:#333}
</style>
</head>
<body>

<div class="abs about-photo" role="img" aria-label="Photo of a desk IP phone with coiled handset cord on a bright surface"></div>

<svg class="abs hero" viewBox="0 0 721 500" aria-hidden="true">
  <defs>
    <linearGradient id="heroFill" x1="0" y1="0" x2="0" y2="1">
      <stop offset="0" stop-color="#1479dc"/>
      <stop offset="1" stop-color="#1a98e8"/>
    </linearGradient>
  </defs>
  <path d="M0 0H721V412Q360 580 0 412Z" fill="url(#heroFill)"/>
</svg>

<div class="abs brand">Calvera</div>
<nav class="abs nav"><span>ABOUT US</span><span>|</span><span>CONTACT US</span></nav>

<div class="abs hero-kicker">ENTERPRISE HD IP PHONE</div>
<h1 class="abs hero-title">CALVERA IP PHONE</h1>
<p class="abs hero-lead">The most affordable IP Phone, with highest compatibility to every IP-PBX system.<br>Sleek designed and user-friendly proven.</p>

<div class="abs product" style="left:58px;top:0">
  <h3>Calvera CV503G</h3>
  <div class="product-image" role="img" aria-label="Product photo of the CV503G desk phone with feature badges"></div>
  <a class="btn-sheet">Download datasheet (EN)</a>
</div>
<div class="abs product" style="left:261px;top:0">
  <h3>Calvera CV505G</h3>
  <div class="product-image" role="img" aria-label="Product photo of the CV505G desk phone with feature badges"></div>
  <a class="btn-sheet">Download datasheet (EN)</a>
</div>
<div class="abs product" style="left:465px;top:0">
  <h3>Calvera CV42</h3>
  <div class="product-image" style="width:96px" role="img" aria-label="Product photo of the CV42 expansion module"></div>
  <a class="btn-sheet">Download datasheet (EN)</a>
</div>

<section class="abs about">
  <h2>ABOUT US</h2>
  <p>Calvera IP Phones is designed with pixel colour LCD with backlight LED, built-in Gigabit Ethernet with up to 28 various features. Equipped with Power over Ethernet (PoE) support, and high definition (HD) sound quality with a rich visual experience. Designed with a fresh appearance, it supports flexible and secured provisioning, deliver modern elegant appearance, superb sound quality and a rich set of IP/SIP telephony features.</p>
</section>

<section class="abs contact" role="img" aria-label="Blue-tinted background photo of a phone keypad"></section>
<div class="abs contact-copy">
  <h2>CONTACT US NOW</h2>
  <h4>Speak to us or send us an enquiry for free consultation.</h4>
  <p>Our team would love to share more about Calvera IP Phones. We are expecting your calls and emails. Drop us an enquiry form at your fingertips!</p>
</div>
<div class="abs field" style="left:279px;top:837px"><svg viewBox="0 0 10 10"><circle cx="5" cy="3" r="2.5"/><path d="M0 10Q5 3 10 10Z"/></svg>First Name</div>
<div class="abs field" style="left:279px;top:873px"><svg viewBox="0 0 10 10"><circle cx="5" cy="3" r="2.5"/><path d="M0 10Q5 3 10 10Z"/></svg>Last Name</div>
<div class="abs field" style="left:279px;top:909px"><svg viewBox="0 0 10 10"><path d="M2 0L4 3 3 4Q4 6 6 7L7 6 10 8 8 10Q0 9 0 2Z"/></svg>Your phone</div>
<div class="abs field" style="left:279px;top:944px"><svg viewBox="0 0 10 10"><path d="M0 2H10V9H0Z M1 3V8H9V3L5 6Z" fill-rule="evenodd"/></svg>Your Email</div>
<div class="abs field message" style="left:470px;top:837px"><svg viewBox="0 0 10 10"><ellipse cx="5" cy="4.5" rx="5" ry="3.5"/><path d="M1 10L2 6 4 7Z"/></svg>How Can we help you?</div>
<div class="abs submit">SUBMIT <svg width="10" height="10" viewBox="0 0 10 10"><path d="M0 4.5L10 0 7.5 10 5 6Z" fill="#fff"/></svg></div>

<div class="abs footer-brand">Calvera</div>
<div class="abs foot-col" style="left:214px;top:1072px">
  <h5>OTHER LINKS</h5>
  <ul><li>About Us</li><li>Contact Us</li></ul>
</div>
<div class="abs foot-col support" style="left:370px;top:1072px;width:190px">
  <h5 style="margin-left:4px">SUPPORT</h5>
  <ul>
    <li><svg viewBox="0 0 10 10"><path d="M5 0A3.5 3.5 0 0 1 8.5 3.5C8.5 6 5 10 5 10S1.5 6 1.5 3.5A3.5 3.5 0 0 1 5 0Z"/></svg>48 Harbourline Road, #07-12,<br>singapore 118420</li>
    <li><svg viewBox="0 0 10 10"><path d="M2 0L4 3 3 4Q4 6 6 7L7 6 10 8 8 10Q0 9 0 2Z"/></svg>6390-4415</li>
    <li><svg viewBox="0 0 10 10"><path d="M0 2H10V9H0Z M1 3V8H9V3L5 6Z" fill-rule="evenodd"/></svg>enquiry@calveratel.com.sg</li>
  </ul>
</div>
<div class="abs foot-col more" style="left:594px;top:1072px">
  <h5>MORE</h5>
  <ul>
    <li><span class="dot"></span>Friendbook</li>
    <li><span class="dot"></span>Chirper</li>
    <li><span class="dot"></span>Workedin</li>
  </ul>
</div>
<div class="abs rule"></div>
<div class="abs copyright">© 2021Calvera. All Rights Reserved</div>

</body>
</html>
```